The Get Me Hired as a Game Producer Business Card Design

I am currently looking for a business card to take along with me to the Play Makers Summit next year. It's my hope to get a business card that is memorable, fun and professional, and will encourage interest in myself and my abilities.

I'm Australian born and raised, and currently live here. I've studied for several years in Game Development and have managed projects professionally as a producer for around 2-3 years now. My job has been referred to as being a 'fire fighter' (hence the 'Game Dev Fire Dept' comment in the contact information). It's my job to prevent problems before they arise or to solve problems for team members as they happen.

I've got skills in time management, team management, project management, empathy, art and programming, as well as a great sense of humor. Whether or not this is something displayed on the card is your choice.

In past I've used a vector image of my face and colors in brown and blue, but this is not a theme I am particularly attached to if you can come up with something better and more creative.

Target Market(s)

Game Developers, Studio Leads, 25 years old and up

Industry/Entity Type

Business

Contact Information for Business Card

Velquaris,
Robert Kanlow,
robert@velquaris.com,
Game Producer/Developer (or Game Dev Fire Dept),

Requirements
Nice to have
• Consideration in the design for (or a second design for) a USB drive card.
http://www.plintrove.com.au/products/slim-usb-card

A space for my twitter account: @Velquaris

```html
<!DOCTYPE html>
<html lang="en">
<head>
<meta charset="utf-8">
<title>Velquaris Business Card</title>
<link rel="stylesheet" href="https://fonts.googleapis.com/css2?family=Roboto+Condensed:wght@300;400&display=swap">
<style>
  :root {
    --navy: #03036b;
    --gap: #ffffff;
    --cyan: #00c8ff;
    --cyan-pale: #8ff4ff;
    --face-front: #12507a;
    --face-back: #0b1c78;
    --name-light: #f3f6ff;
    --text-light: #e6ecff;
  }
  * { margin: 0; padding: 0; box-sizing: border-box; }
  html, body { width: 1200px; height: 938px; overflow: hidden; background: var(--gap); }
  .sheet { position: relative; width: 1200px; height: 938px; }
  .card {
    position: absolute; top: 0; width: 579px; height: 938px;
    background: var(--navy); overflow: hidden;
  }
  .card--front { left: 0; }
  .card--back { left: 621px; }

  .portrait { position: absolute; }
  .portrait--front {
    left: 38px; top: 76px; width: 296px; height: 431px;
    background: var(--face-front);
    border: 8px solid #1a1a1a;
    border-radius: 48% 48% 46% 46% / 40% 40% 60% 60%;
  }
  .portrait--back {
    left: -10px; top: -40px; width: 336px; height: 581px;
    background: var(--face-back);
    border: 8px solid #22236a;
    border-radius: 46% 46% 48% 48% / 36% 36% 64% 64%;
  }

  .flourish {
    position: absolute;
    background: linear-gradient(135deg, var(--cyan) 0%, var(--cyan-pale) 45%, var(--cyan) 70%, #1aa6e8 100%);
  }
  .flourish--top {
    right: 0; top: 0; width: 241px; height: 350px;
    clip-path: polygon(0 0, 100% 0, 100% 100%, 80% 95%, 55% 78%, 25% 50%, 5% 22%);
  }
  .flourish--bottom {
    left: 0; bottom: 0; width: 245px; height: 355px;
    clip-path: polygon(0 0, 20% 5%, 45% 22%, 75% 50%, 95% 78%, 100% 100%, 0 100%);
  }

  .vertical {
    position: absolute;
    writing-mode: vertical-rl;
    transform: rotate(180deg);
    white-space: nowrap;
  }
  .brand-name {
    left: 330px; top: 435px; height: 440px; width: 84px;
    font-family: "Roboto Condensed", sans-serif; font-weight: 400;
    font-size: 78px; line-height: 84px; letter-spacing: 4px;
    color: var(--name-light);
    text-align: left;
  }
  .person-name {
    left: 307px; top: 456px; height: 444px; width: 72px;
    font-family: "Roboto Condensed", sans-serif; font-weight: 400;
    font-size: 60px; line-height: 72px; letter-spacing: 1px;
    color: var(--name-light);
    text-align: left;
  }
  .rule {
    position: absolute; top: 448px; width: 11px; height: 456px;
    background: linear-gradient(to bottom, var(--cyan-pale) 0 38%, var(--cyan) 38% 100%);
  }
  .rule--left { left: 403px; }
  .rule--right { left: 455px; }
  .job-title {
    left: 421px; top: 452px; height: 443px; width: 28px;
    font-family: "Roboto Condensed", sans-serif; font-weight: 300;
    font-size: 22px; letter-spacing: 2.6px; line-height: 28px;
    color: var(--text-light); text-align: left;
  }
  .contact {
    font-family: "Roboto Condensed", sans-serif; font-weight: 400;
    font-size: 24px; line-height: 30px; color: var(--text-light);
    text-align: left;
  }
  .contact--phone { left: 479px; top: 600px; height: 291px; width: 30px; }
  .contact--email { left: 519px; top: 440px; height: 451px; width: 30px; }
</style>
</head>
<body>
<main class="sheet">
  <section class="card card--front">
    <div class="flourish flourish--top" role="img" aria-label="Decorative cyan feather-like flourish with diagonal stripes"></div>
    <div class="flourish flourish--bottom" role="img" aria-label="Decorative cyan feather-like flourish with diagonal stripes"></div>
    <div class="portrait portrait--front" role="img" aria-label="Vector illustration of a bearded man's head"></div>
    <div class="vertical brand-name">Velquaris</div>
  </section>

  <section class="card card--back">
    <div class="portrait portrait--back" role="img" aria-label="Faint oversized vector illustration of a bearded man's head"></div>
    <div class="flourish flourish--top" role="img" aria-label="Decorative cyan feather-like flourish with diagonal stripes"></div>
    <div class="flourish flourish--bottom" role="img" aria-label="Decorative cyan feather-like flourish with diagonal stripes"></div>
    <div class="vertical person-name">Robert Kanlow,</div>
    <div class="rule rule--left"></div>
    <div class="vertical job-title">GAME PRODUCER / DEVELOPER</div>
    <div class="rule rule--right"></div>
    <div class="vertical contact contact--phone">Phone : 61 400 518 372</div>
    <div class="vertical contact contact--email">Email &nbsp;: robert@velquaris.com,</div>
  </section>
</main>
</body>
</html>
```